Creative designer wanted for unique pet treats product packaging!

My company is "Tailwag Pantry!" and we're a new and upcoming premium pet treat company. We are different than the rest as we have core values that really stand out and that we're VERY passionate about. They are the following:
HEALTHY-All of our ingredients are fresh and wholesome for dogs. Each has unique health benefits for dogs and there is never any filler-just the good stuff.
AMOUNT OF INGREDIENTS-Most of dog treats have large lists of ingredients and often many of those are difficult to pronounce or people have to look up what they even are. Often there is lot of "filler". We pride ourselves on just having a few ingredients or less. Every ingredient can easily be pronounced, recognized and are commonly consumed by humans in regular meals.
GIVING BACK- We donate a portion of the proceeds of every bag to go to hand selected, accredited and legit animals charities and rescues.
ENVIRONMENT- We strongly care about the environment which is why our bags are compostable. Just simply remove the zipper and track then put the bag in a composting bin. Easy as that. (We have attached a "how to compost your bag in 2 simple steps" image that we would like shown on the bags.
Our initial product is Maple Sage Crunchy Bark-ley Bites. The ingredients are: Coconut oil, dill, and sweet potato.
We want a design that embodies our values. As well, we have attached "our story" that describes the company and what we are about to consumers. We would like to have it put on the package, but if it cannot be done, then just the meat and potatoes of the message.
A good example for recognition is the attached cake mix as it's simple, portrays the product nicely and when seen from afar-it is easily identified.
*We would like to have a window on the bag that is similar to our paw and leaf logo.
We would also like to see the color green on the package.
Bag specifics are:
Size: 250g OPTIMIZED
Dimensions Inches: 6.15''x9.41''x3.50''
Dimensions mm : 156x239x89
Type: Stand-Up Pouch with Zip (PLOW)
COMPOSTABLE
Material: 100NK MATTE/70NKA/3mil BIOPBS
CMYKW

```html
<!DOCTYPE html>
<html lang="en">
<head>
<meta charset="utf-8">
<title>Tailwag Pantry! – Maple Sage Crunchy Bark-ley Bites pouch</title>
<link rel="stylesheet" href="https://fonts.googleapis.com/css2?family=Fjalla+One&family=Mulish:wght@300;700;800&family=Roboto:wght@700&display=swap">
<style>
  :root {
    --bg: #d9dadb;
    --green: #1f8a3a;
    --green-dark: #0f5a2c;
    --green-deep: #0b4a24;
    --leaf: #7cc242;
    --brown: #8a5a2b;
    --yellow: #f4e04d;
    --silver: #c9cacc;
    --silver-light: #eeeeef;
    --white: #ffffff;
    --ink: #3a3a3a;
  }
  * { box-sizing: border-box; margin: 0; padding: 0; }
  html, body { width: 1200px; height: 1200px; overflow: hidden; }
  body {
    background: radial-gradient(ellipse at 50% 60%, #ececec 0%, var(--bg) 75%);
    position: relative;
    font-family: "Mulish", sans-serif;
  }
  .pouch { position: absolute; top: 318px; width: 414px; height: 578px; overflow: hidden; }
  .pouch--front { left: 158px; background: linear-gradient(180deg, var(--green) 0%, #25963f 55%, var(--green-dark) 100%); }
  .pouch--back { left: 638px; background: linear-gradient(180deg, var(--silver-light) 0%, #f7f7f7 50%, #e6e6e7 100%); }
  .pouch__shapes { position: absolute; inset: 0; }

  .brand { position: absolute; display: flex; align-items: center; gap: 6px; color: var(--brown);
    font-family: "Mulish", sans-serif; font-weight: 800; white-space: nowrap; }
  .brand__dot { width: 12px; height: 12px; border-radius: 50%; background: var(--leaf); flex: none; }
  .pouch--front .brand { left: 270px; top: 108px; font-size: 15px; color: var(--leaf); }
  .pouch--back .brand { left: 0; right: 0; justify-content: center; top: 132px; font-size: 21px; color: var(--green); }
  .pouch--back .brand__dot { width: 16px; height: 16px; }

  .product-name { position: absolute; left: 0; width: 414px; text-align: center; }
  .product-name__flavour { display: block; position: absolute; left: 40px; width: 330px; top: 140px;
    font-family: "Fjalla One", sans-serif; font-size: 58px; line-height: 1; color: var(--white);
    -webkit-text-stroke: 1.5px var(--green-deep); text-align: center; }
  .product-name__line { display: block; position: absolute; left: 40px; width: 330px; top: 208px;
    font-family: "Fjalla One", sans-serif; font-size: 19px; color: var(--yellow);
    -webkit-text-stroke: 0.5px #6a5a10; text-align: center; }

  .ingredients { position: absolute; left: 256px; top: 245px; list-style: none; }
  .ingredients li { margin-bottom: 12px; font-family: "Fjalla One", sans-serif; font-size: 13px; line-height: 16px;
    padding: 1px 7px; border: 1.5px solid var(--white); border-radius: 5px; display: table; }
  .ingredients .oil { color: var(--brown); background: var(--silver-light); }
  .ingredients .dill { color: var(--white); background: var(--green); margin-left: 6px; }
  .ingredients .potato { color: var(--yellow); background: var(--green); margin-left: 8px; }

  .net-weight { position: absolute; left: 80px; top: 494px; font-family: "Roboto", sans-serif; font-weight: 700;
    font-size: 22px; color: var(--white); }

  .story { position: absolute; left: 50px; right: 50px; top: 196px; text-align: center;
    font-size: 8.6px; line-height: 12.8px; font-weight: 300; color: var(--ink); }
  .story p + p { margin-top: 12px; }
  .story u { text-decoration: underline; }

  .compost { position: absolute; left: 64px; top: 436px; width: 270px; height: 57px;
    border: 1.5px solid #9a9a9a; background: #8fc6a0; padding: 2px; }
  .compost__title { background: var(--green); color: var(--white); font-family: "Fjalla One", sans-serif;
    font-size: 6.5px; padding: 1px 20px; letter-spacing: 0.2px; }
  .compost__steps { display: flex; gap: 8px; padding: 4px 4px 0; }
  .compost__step { display: flex; gap: 4px; flex: 1; }
  .compost__art { width: 26px; height: 30px; background: linear-gradient(180deg,#e8f2f8,#5e7d6a); flex: none; }
  .compost__text { color: var(--white); font-size: 4px; line-height: 5px; font-weight: 700; }
  .compost__text strong { display: block; font-family: "Fjalla One", sans-serif; font-size: 6px; line-height: 7px; font-weight: 400; }
</style>
</head>
<body>

<section class="pouch pouch--front" aria-label="Front of pouch">
  <svg class="pouch__shapes" width="414" height="578" viewBox="0 0 414 578">
    <defs>
      <radialGradient id="heroTone" cx="0.5" cy="0.45" r="0.6">
        <stop offset="0" stop-color="#f4f4f4"/>
        <stop offset="1" stop-color="#b9bbbd"/>
      </radialGradient>
      <linearGradient id="windowTone" x1="0" y1="0" x2="1" y2="1">
        <stop offset="0" stop-color="#b4b6b8"/>
        <stop offset="1" stop-color="#8f9194"/>
      </linearGradient>
    </defs>
    <circle class="brand-disc" cx="372" cy="56" r="140" fill="var(--green-deep)"/>
    <path d="M232 128 Q320 170 414 150" stroke="var(--leaf)" stroke-width="3" fill="none" opacity="0.7"/>
    <circle cx="154" cy="304" r="184" fill="url(#heroTone)" role="img" aria-label="Photo of a happy white terrier with its tongue out"/>
    <rect x="170" y="322" width="204" height="196" rx="60" fill="url(#windowTone)" role="img" aria-label="Clear window showing the treats inside"/>
    <path d="M0 540 Q200 490 414 520" stroke="var(--leaf)" stroke-width="3" fill="none" opacity="0.6"/>
    <path d="M0 560 Q220 520 414 545 L414 578 L0 578 Z" fill="var(--green-deep)" opacity="0.5"/>
  </svg>

  <div class="brand"><span class="brand__dot"></span>Tailwag Pantry!</div>

  <h1 class="product-name">
    <span class="product-name__flavour">Maple Sage</span>
    <span class="product-name__line">Crunchy Bark-ley Bites</span>
  </h1>

  <ul class="ingredients">
    <li class="oil">COCONUT OIL</li>
    <li class="dill">DILL</li>
    <li class="potato">SWEET POTATO</li>
  </ul>

  <p class="net-weight">Net. 250g</p>
</section>

<section class="pouch pouch--back" aria-label="Back of pouch">
  <div class="brand"><span class="brand__dot"></span>Tailwag Pantry!</div>

  <div class="story">
    <p>we are a local Brookvale pet treat company that emerged from an unwavering passion for supporting the pet community,<br>as well as providing pets a healthy alternative with just a <u>few</u> or <u>less</u> ingredients.<br>We always use fresh ingredients and we make each bag with love, just as though we are creating it for our children because --lets face it--our pets are our children. Further,<br>at Tailwag Pantry, we are committed to using a portion of our product proceeds to help local animal shelters. By doing so, we are creating a better world for all of our best friends.</p>
    <p>Our company was built on the foundation of giving back.<br>We focus on ensuring that our donations aid rescues, shelters, charities and more to guarantee that our furry friends are taken off the streets and placed in loving homes where they receive food, medication and the care that they so need and deserve.</p>
  </div>

  <div class="compost">
    <div class="compost__title">"HOW TO COMPOST YOUR BAG IN 2 SIMPLE STEPS!</div>
    <div class="compost__steps">
      <div class="compost__step">
        <div class="compost__art" role="img" aria-label="Illustration of cutting the zipper off the bag"></div>
        <p class="compost__text"><strong>STEP 1.</strong>Cut off zipper and track, recycle in blue bin</p>
      </div>
      <div class="compost__step">
        <div class="compost__art" role="img" aria-label="Illustration of a green compost bin"></div>
        <p class="compost__text"><strong>STEP 2.</strong>Place bag in green bin for composting</p>
      </div>
      <div class="compost__step">
        <div class="compost__art" role="img" aria-label="Illustration of sun over soil"></div>
        <p class="compost__text"><strong>FOR BEST RESULTS IN COMPOSTING:</strong>Heat, moisture and microbes</p>
      </div>
    </div>
  </div>
</section>

</body>
</html>
```